GKL Auto - help to get me noticed

We not long ago tasked Pixel Harbor to design a logo for my business. I'm happy with the result so would like to have a business card designed as a follow up.

It's an Automotive service and repair business that offers the following -
- Servicing
- General repairs
- Brakes
- Detailing
- Integrity

GKL Automotive
Malcolm Pryde
0491 726 183

Target Market(s)

Everyday people with the ability to reach out to corporate customers also.

Industry/Entity Type

Automotive

Contact Information for Business Card

Black card, logo, name and phone number on front. Other details on back of card.

```html
<!DOCTYPE html>
<html lang="en">
<head>
<meta charset="UTF-8">
<title>GKL Automotive – Business Card</title>
<link href="https://fonts.googleapis.com/css2?family=Noto+Serif:ital,wght@0,400;0,700;1,400;1,700&family=Exo+2:wght@600&display=swap" rel="stylesheet">
<style>
  :root {
    --backdrop: #2e3e46;
    --card-white: #ffffff;
    --card-black: #1a1a1a;
    --brand-green: #55981f;
    --ink-navy: #2e3560;
    --ink-dark: #222222;
    --icon-blue: #2a9fd8;
    --text-light: #ffffff;
  }
  * { box-sizing: border-box; margin: 0; padding: 0; }
  html, body {
    width: 1200px; height: 900px; overflow: hidden;
    background: var(--backdrop);
  }
  .canvas {
    width: 1200px; height: 900px;
    display: flex; flex-direction: column; align-items: center; justify-content: center;
    gap: 40px;
  }
  .card {
    width: 640px; height: 366px; position: relative; overflow: hidden;
    box-shadow: 0 10px 30px rgba(0,0,0,.35);
  }

  /* Back side */
  .card-back {
    background: var(--card-white);
    font-family: "Noto Serif", serif;
  }
  .intro {
    position: absolute; top: 30px; left: 0; right: 0; text-align: center;
    color: var(--brand-green); font-style: italic; font-weight: 700; font-size: 12.5px;
  }
  .services {
    position: absolute; top: 58px; left: 196px;
    display: grid; grid-template-columns: 150px 160px; row-gap: 6px;
    list-style: none; color: var(--ink-navy); font-weight: 700; font-size: 11.5px;
  }
  .services li { display: flex; align-items: center; gap: 10px; }
  .services li::before {
    content: ""; width: 10px; height: 7px; border-radius: 50%; background: var(--brand-green);
  }
  .services .col-2 { grid-column: 2; }
  .signature {
    position: absolute; top: 146px; right: 40px; text-align: right;
  }
  .signature .name { color: var(--brand-green); font-weight: 700; font-size: 19px; line-height: 1.1; }
  .signature .title { color: var(--ink-dark); font-weight: 700; font-size: 12px; }
  .divider {
    position: absolute; top: 185px; left: 36px; width: 520px; height: 1.5px; background: var(--brand-green);
  }
  .contacts {
    position: absolute; top: 205px; left: 36px; list-style: none;
    font-style: italic; font-size: 16px; color: var(--ink-dark);
  }
  .contacts li { display: flex; align-items: center; gap: 16px; height: 34px; }
  .contacts svg { width: 18px; height: 18px; stroke: var(--icon-blue); fill: none; stroke-width: 1.4; }

  /* Front side */
  .card-front { background: var(--card-black); }
  .wordmark {
    position: absolute; top: 0; left: 0; right: 0; bottom: 50px;
    display: flex; align-items: center; justify-content: center;
    font-family: "Exo 2", sans-serif; font-weight: 600; font-size: 64px;
    color: var(--brand-green); letter-spacing: 2px; text-transform: uppercase;
  }
  .phone-band {
    position: absolute; left: 0; right: 0; bottom: 0; height: 50px;
    background: var(--brand-green); color: var(--text-light);
    display: flex; align-items: center; justify-content: center;
    font-family: "Exo 2", sans-serif; font-weight: 600; font-size: 20px;
  }
</style>
</head>
<body>
<main class="canvas">
  <section class="card card-back">
    <p class="intro">It's an Automotive service and repair business that offers the following</p>
    <ul class="services">
      <li>Servicing</li>
      <li>General repairs</li>
      <li>Brakes</li>
      <li>Detailing</li>
      <li>Integrity</li>
    </ul>
    <div class="signature">
      <p class="name">Your Name</p>
      <p class="title">Your Title</p>
    </div>
    <div class="divider"></div>
    <ul class="contacts">
      <li>
        <svg viewBox="0 0 20 20"><circle cx="10" cy="10" r="8.5"/><path d="M7.5 5.5c-1.5 1-1.5 3 0 5.5s3.5 4 5 3.5l.8-1.3-1.8-1.3-1 .6c-1-.6-1.8-1.6-2.3-2.7l.8-.8-.9-2z"/></svg>
        0407 318 265
      </li>
      <li>
        <svg viewBox="0 0 20 20"><rect x="1.5" y="4.5" width="17" height="11"/><path d="M1.5 4.5l8.5 7 8.5-7M1.5 15.5l6-5M18.5 15.5l-6-5"/></svg>
        email @yourweb.com
      </li>
      <li>
        <svg viewBox="0 0 20 20"><circle cx="10" cy="10" r="8.5"/><ellipse cx="10" cy="10" rx="3.8" ry="8.5"/><path d="M1.5 10h17M3 5.5h14M3 14.5h14M10 1.5v17"/></svg>
        www.yourweb.com
      </li>
    </ul>
  </section>

  <section class="card card-front">
    <h1 class="wordmark">GKL Automotive</h1>
    <p class="phone-band">0491 726 183</p>
  </section>
</main>
</body>
</html>
```